Fitness Centre/Personal Trainer Business Card

We need a business card design for a company based in Singapore called 'Vigor Summit'.

We are a team of Personal Trainers and we are planning to open our new training facility.

This design will also be printed/painted on the walls in our gym.

We are a new breed of personal trainers who take fitness seriously and holistically. We do not merely train our clients to be big and muscular.

We believe in wholeness. In our opinion, fitness should include: strength, speed, flexibility, mobility, stamina & agility. These are what we train for. Of course, nutrition/diet is key.

We use fitness tools such as kettlebells, QLV, Pylometric boxes, battling ropes, clubbells, medicine balls, bulgarian bags etc - functional and non-bulky tools.

I currently have a Facebook page 'Vigor Summit SG' which shows a logo of a kettlebell. But my business focus has since changed.

Services provided:
- Kettlebell Sport Preparation
- Calisthenics Training
- Corrective Exercises
- Sports Strength & Conditioning
- 28 days Weight Loss Program
- Myofascial Rehab Therapy
- Sports/Thai Massage

Main colors for the design should be BLACK & YELLOW. We envision a design which is able to protray the holistic view we take on fitness. Also it should somewhat appeal to the ladies and not intimidate them.

Target Market(s)

People between 18-35 years old. Students and working class alike.

Industry/Entity Type

Training

Requirements
Must have
• Name: Marcus Oleander Pryce
Fitness Coach
Corrective Exercise Specialist
M: +65 9372 6058
E: marcus@sgvigorsummit-example.com

Double-sided please.
Nice to have
• "What is your vigor summit?"

```html
<!DOCTYPE html>
<html lang="en">
<head>
<meta charset="utf-8">
<title>Vigor Summit – Business Cards</title>
<link rel="stylesheet" href="https://fonts.googleapis.com/css2?family=Open+Sans:wght@400;600;700&display=swap">
<style>
  :root {
    --backdrop: #e4e4e2;
    --card-black: #050505;
    --card-grey: #6e6e6e;
    --card-charcoal: #2c2c2c;
    --yellow: #f3d21a;
    --white: #ffffff;
    --soft-white: #e9e9e9;
  }
  * { box-sizing: border-box; margin: 0; padding: 0; }
  html, body { width: 1200px; height: 722px; overflow: hidden; }
  body {
    background: var(--backdrop);
    font-family: "Open Sans", Arial, sans-serif;
    position: relative;
  }
  .card {
    position: absolute;
    width: 488px;
    height: 280px;
    border-radius: 14px;
    overflow: hidden;
    background: var(--card-black);
    color: var(--white);
  }
  .card--front { left: 96px; top: 65px; }
  .card--photo-back { left: 614px; top: 65px; }
  .card--list-back { left: 99px; top: 370px; background: linear-gradient(90deg, #1e1e1e 0%, #3a3a3a 100%); }
  .card--centered-back { left: 614px; top: 377px; }

  /* brand name block (stands where the mark would be) */
  .brand {
    position: absolute;
    display: flex;
    align-items: center;
    gap: 8px;
    color: var(--yellow);
    font-weight: 700;
    font-size: 26px;
    line-height: 1;
    white-space: nowrap;
  }
  .brand__dot {
    width: 16px; height: 16px;
    border-radius: 50%;
    background: var(--yellow);
    flex: none;
  }

  /* front */
  .front__band {
    position: absolute; left: 0; top: 0; width: 100%; height: 88px;
    background: var(--card-grey);
  }
  .front__rule {
    position: absolute; left: 0; top: 90px; width: 100%; height: 3px;
    background: var(--yellow);
  }
  .front .brand { left: 40px; top: 160px; }
  .front__question {
    position: absolute; left: 262px; top: 30px;
    font-weight: 700; font-size: 19px; line-height: 25px;
    text-transform: uppercase;
  }
  .front__details { position: absolute; left: 262px; top: 118px; }
  .front__name {
    color: var(--yellow); font-size: 19px; font-weight: 600;
    text-transform: uppercase; letter-spacing: 0.2px; margin-bottom: 3px;
  }
  .front__role { font-size: 12px; line-height: 17px; }
  .front__contact { margin-top: 14px; font-size: 12px; line-height: 18px; }
  .contact-line { display: flex; align-items: center; gap: 5px; }
  .contact-line svg { width: 8px; height: 9px; fill: var(--yellow); }
  .front__web { margin-top: 18px; font-size: 12.5px; letter-spacing: 0.6px; }

  /* photo back */
  .photo-back__image {
    position: absolute; inset: 0;
    background: radial-gradient(ellipse at 35% 75%, #6a6a6a 0%, #2e2e2e 40%, #050505 80%);
  }
  .photo-back .brand { left: 40px; top: 65px; font-size: 22px; }
  .services { position: absolute; }
  .services__title { font-weight: 700; font-size: 18px; }
  .services__list { list-style: none; }
  .photo-back .services { right: 16px; top: 38px; text-align: right; }
  .photo-back .services__title { font-size: 18px; margin-bottom: 13px; }
  .photo-back .services__list li {
    color: var(--yellow); font-weight: 700; font-size: 14.5px; line-height: 28px;
  }

  /* list back */
  .list-back .brand { left: 40px; top: 128px; }
  .list-back .services { left: 250px; top: 42px; }
  .list-back .services__title { color: var(--yellow); font-size: 18px; margin-bottom: 14px; }
  .list-back .services__list li { font-size: 14px; line-height: 24.5px; color: var(--soft-white); }

  /* centered back */
  .centered-back__faint {
    position: absolute; left: 0; right: 0; top: 120px;
    text-align: center; color: var(--yellow); opacity: 0.22;
    font-weight: 700; font-size: 58px; line-height: 1;
  }
  .centered-back__title {
    position: absolute; left: 0; right: 0; top: 56px;
    text-align: center; font-weight: 700; font-size: 18px;
  }
  .centered-back__rows {
    position: absolute; left: 0; right: 0; top: 120px;
    text-align: center; font-size: 16px; line-height: 30px; color: var(--soft-white);
  }
</style>
</head>
<body>

<!-- Front -->
<section class="card card--front front">
  <div class="front__band"></div>
  <div class="front__rule"></div>
  <div class="brand"><span class="brand__dot"></span>Vigor Summit</div>
  <h1 class="front__question">What is your<br>vigor summit ?</h1>
  <div class="front__details">
    <p class="front__name">Marcus Oleander Pryce</p>
    <p class="front__role">Fitness Coach<br>Corrective Exercise Specialist</p>
    <div class="front__contact">
      <p class="contact-line">
        <svg viewBox="0 0 8 10" aria-hidden="true"><rect x="1" y="0" width="6" height="10" rx="1"/></svg>
        +65 9372 6058
      </p>
      <p class="contact-line">
        <svg viewBox="0 0 10 8" aria-hidden="true"><rect x="0" y="0" width="10" height="8" rx="1"/></svg>
        marcus@sgvigorsummit-example.com
      </p>
    </div>
    <p class="front__web">www.sgvigorsummit-example.com</p>
  </div>
</section>

<!-- Back, photo version -->
<section class="card card--photo-back photo-back">
  <div class="photo-back__image" role="img" aria-label="Photo of hexagonal dumbbells on a dark floor"></div>
  <div class="brand"><span class="brand__dot"></span>Vigor Summit</div>
  <div class="services">
    <h2 class="services__title">Services</h2>
    <ul class="services__list">
      <li>• Sports Strength &amp; Conditioning</li>
      <li>• Kettlebell Sport Preparation</li>
      <li>• 28 days Weight Loss Program</li>
      <li>• Myofascial Rehab Therapy</li>
      <li>• Calisthenics Training</li>
      <li>• Corrective Exercises</li>
      <li>• Sports/Thai Massage</li>
    </ul>
  </div>
</section>

<!-- Back, list version -->
<section class="card card--list-back list-back">
  <div class="brand"><span class="brand__dot"></span>Vigor Summit</div>
  <div class="services">
    <h2 class="services__title">Services</h2>
    <ul class="services__list">
      <li>• Sports Strength &amp; Conditioning</li>
      <li>• Kettlebell Sport Preparation</li>
      <li>• 28 days Weight Loss Program</li>
      <li>• Myofascial Rehab Therapy</li>
      <li>• Calisthenics Training</li>
      <li>• Corrective Exercises</li>
      <li>• Sports/Thai Massage</li>
    </ul>
  </div>
</section>

<!-- Back, centered version -->
<section class="card card--centered-back centered-back">
  <p class="centered-back__faint" aria-hidden="true">Vigor Summit</p>
  <h2 class="centered-back__title">Services</h2>
  <div class="centered-back__rows">
    <p>• Sports Strength &amp; Conditioning &nbsp;• Sports/Thai Massage</p>
    <p>• Kettlebell Sport Preparation &nbsp;• Corrective Exercises</p>
    <p>• 28 days Weight Loss Program &nbsp;• Calisthenics Training</p>
    <p>• Myofascial Rehab Therapy</p>
  </div>
</section>

</body>
</html>
```